Homepage of voice message app

We are developing a mobile application of which one of the more important features is a voice to transcript.

What we would like to have designed is a basic interface that would show one ore more avatars on a home screen + the following functionalities:
- record
-while recording there should be three functions included in buttons (delete last sentence / send / send & next message (i.e. keep the recording going))
&
- listen (to new message)
- while listening replies should be possible in the form of emoticons (only emoticons, no text)

Attached:
-an example of the style we appreciate

Target Market(s)

English speaking Millenials

Industry/Entity Type

Messaging

Font styles to use
Sans Serif

Requirements
Must have
• My project must have a clean design and should not be too futuristic. We are targetting an average person between 20-80 years.
Nice to have
• We would like to focus on a minimum amount of finger movements to get the message across, we prefer simple tabs and swipes within the home screen to access the features.
Should not have
• The project should not have too many moving pieces within the screen.

```html
<!DOCTYPE html>
<html lang="en">
<head>
<meta charset="utf-8">
<title>Voice message app – home screens</title>
<link rel="stylesheet" href="https://fonts.googleapis.com/css2?family=Poppins:wght@400;500;600&display=swap">
<style>
  :root{
    --canvas:#f2f3f6;
    --blue-top:#2196f6;
    --blue-mid:#3f6cf2;
    --violet-bottom:#5b3ff0;
    --orb-light:#3a86f5;
    --orb-dark:#2f4fe0;
    --white:#ffffff;
    --card-text:#9aa0ac;
    --red:#f2546b;
    --btn-blue:#2f7bf3;
    --btn-soft:rgba(255,255,255,.18);
    --caption:rgba(255,255,255,.78);
    --avatar-a:#7fb2ff;
    --avatar-b:#9a86ff;
    --avatar-c:#5fd0e8;
  }
  *{box-sizing:border-box;margin:0;padding:0}
  html,body{width:1200px;height:2288px;overflow:hidden;background:var(--canvas);font-family:"Poppins",sans-serif}
  .board{position:relative;width:1200px;height:2288px}
  .screen{
    position:absolute;width:270px;height:550px;border-radius:26px;overflow:hidden;
    background:linear-gradient(180deg,var(--blue-top) 0%,var(--blue-mid) 55%,var(--violet-bottom) 100%);
    box-shadow:0 18px 40px rgba(40,60,120,.18);
  }
  .orb{
    position:absolute;left:50%;width:116px;height:116px;margin-left:-58px;border-radius:50%;
    background:radial-gradient(circle at 40% 30%,var(--orb-light),var(--orb-dark));
    box-shadow:0 14px 30px rgba(20,30,120,.35);
    display:flex;align-items:center;justify-content:center;
  }
  .orb svg{width:62px;height:62px}
  .caption{position:absolute;left:0;right:0;text-align:center;font-size:10px;line-height:14px;color:var(--caption);letter-spacing:.3px}

  /* home */
  .screen--home .orb{top:200px}
  .screen--home .caption{top:340px}
  .contacts{position:absolute;top:420px;left:0;right:0;display:flex;justify-content:center;gap:14px}
  .avatar{width:34px;height:34px;border-radius:50%;display:flex;align-items:center;justify-content:center;
    font-size:11px;font-weight:500;color:var(--white);border:2px solid rgba(255,255,255,.55)}
  .avatar--a{background:var(--avatar-a)}
  .avatar--b{background:var(--avatar-b)}
  .avatar--c{background:var(--avatar-c)}

  /* recording */
  .screen--recording .orb{top:120px}
  .controls{position:absolute;top:360px;left:0;right:0;display:flex;justify-content:center;gap:26px}
  .control{width:34px;height:34px;border-radius:50%;background:var(--btn-soft);display:flex;align-items:center;justify-content:center}
  .control--delete{background:var(--red)}
  .control svg{width:16px;height:16px}
  .send-pill{position:absolute;top:470px;left:50%;width:112px;margin-left:-56px;height:30px;border-radius:15px;background:var(--white);
    color:var(--btn-blue);font-size:11px;font-weight:600;display:flex;align-items:center;justify-content:center;box-shadow:0 8px 18px rgba(20,30,120,.25)}

  /* listening */
  .screen--listening .orb{top:200px}
  .screen--listening .caption{top:340px}
  .reactions{position:absolute;top:410px;left:0;right:0;display:flex;justify-content:center;gap:16px}
  .reaction{width:34px;height:34px;border-radius:50%;background:var(--btn-soft);display:flex;align-items:center;justify-content:center}
  .reaction svg{width:16px;height:16px}

  /* transcript */
  .screen--transcript .orb{top:80px;width:96px;height:96px;margin-left:-48px}
  .screen--transcript .orb svg{width:50px;height:50px}
  .transcript-card{position:absolute;left:0;right:0;top:240px;bottom:0;background:var(--white);border-radius:22px 22px 0 0;padding:26px 24px 0}
  .transcript-text{font-size:10.5px;line-height:1.75;color:var(--card-text)}
  .card-action{position:absolute;bottom:22px;width:32px;height:32px;border-radius:50%;display:flex;align-items:center;justify-content:center}
  .card-action svg{width:14px;height:14px}
  .card-action--delete{left:22px;background:var(--red)}
  .card-action--send{right:22px;background:var(--btn-blue)}
</style>
</head>
<body>
<svg width="0" height="0" style="position:absolute" aria-hidden="true">
  <symbol id="mic" viewBox="0 0 64 64">
    <g fill="none" stroke="#fff" stroke-width="2.6" stroke-linecap="round">
      <rect x="25" y="12" width="14" height="26" rx="7"/>
      <path d="M19 31a13 13 0 0 0 26 0"/>
      <path d="M32 44v8M25 52h14"/>
      <path d="M13 22v8M17 18v16M47 18v16M51 22v8"/>
    </g>
  </symbol>
  <symbol id="play" viewBox="0 0 64 64">
    <path d="M25 18l22 14-22 14z" fill="#fff"/>
  </symbol>
  <symbol id="trash" viewBox="0 0 16 16"><g fill="none" stroke="#fff" stroke-width="1.5" stroke-linecap="round"><path d="M3 4h10M6 4V2.5h4V4M4.5 4l.7 9.5h5.6L11.5 4"/></g></symbol>
  <symbol id="stop" viewBox="0 0 16 16"><rect x="4.5" y="4.5" width="7" height="7" rx="1.5" fill="#fff"/></symbol>
  <symbol id="undo" viewBox="0 0 16 16"><g fill="none" stroke="#fff" stroke-width="1.5" stroke-linecap="round" stroke-linejoin="round"><path d="M6 4L3 7l3 3"/><path d="M3 7h6a4 4 0 0 1 0 8H7"/></g></symbol>
  <symbol id="send" viewBox="0 0 16 16"><path d="M2 8l12-6-4 12-2-5z" fill="#fff"/></symbol>
  <symbol id="heart" viewBox="0 0 16 16"><path d="M8 14S2 10.2 2 6.2A3.2 3.2 0 0 1 8 4.6a3.2 3.2 0 0 1 6 1.6C14 10.2 8 14 8 14z" fill="#fff"/></symbol>
  <symbol id="tick" viewBox="0 0 16 16"><path d="M3 8.5l3 3 7-7" fill="none" stroke="#fff" stroke-width="1.8" stroke-linecap="round" stroke-linejoin="round"/></symbol>
  <symbol id="star" viewBox="0 0 16 16"><path d="M8 1.8l1.9 3.9 4.3.6-3.1 3 .7 4.3L8 11.6l-3.8 2 .7-4.3-3.1-3 4.3-.6z" fill="#fff"/></symbol>
  <symbol id="bolt" viewBox="0 0 16 16"><path d="M9 1.5L3.5 9H8l-1 5.5L12.5 7H8z" fill="#fff"/></symbol>
</svg>

<main class="board">
  <!-- top row -->
  <section class="screen screen--recording" style="left:30px;top:120px">
    <div class="orb"><svg><use href="#mic"/></svg></div>
    <div class="controls">
      <span class="control" aria-label="Delete last sentence"><svg><use href="#undo"/></svg></span>
      <span class="control" aria-label="Send and keep recording"><svg><use href="#stop"/></svg></span>
      <span class="control control--delete" aria-label="Delete"><svg><use href="#trash"/></svg></span>
    </div>
    <div class="send-pill">Send</div>
  </section>
  <section class="screen screen--home" style="left:320px;top:260px">
    <div class="orb"><svg><use href="#mic"/></svg></div>
    <p class="caption">Tap to record</p>
    <div class="contacts">
      <span class="avatar avatar--a">AL</span>
      <span class="avatar avatar--b">SM</span>
      <span class="avatar avatar--c">JO</span>
    </div>
  </section>
  <section class="screen screen--transcript" style="left:610px;top:120px">
    <div class="orb"><svg><use href="#mic"/></svg></div>
    <div class="transcript-card">
      <p class="transcript-text">Hi Sam, just leaving a quick note about tomorrow. The meeting moved to ten so we can grab coffee first. Let me know if that still works for you and the team.</p>
      <span class="card-action card-action--delete"><svg><use href="#trash"/></svg></span>
      <span class="card-action card-action--send"><svg><use href="#send"/></svg></span>
    </div>
  </section>
  <section class="screen screen--home" style="left:900px;top:260px">
    <div class="orb"><svg><use href="#mic"/></svg></div>
    <p class="caption">Tap to record</p>
    <div class="contacts">
      <span class="avatar avatar--a">AL</span>
      <span class="avatar avatar--b">SM</span>
      <span class="avatar avatar--c">JO</span>
    </div>
  </section>

  <!-- lower set -->
  <section class="screen screen--recording" style="left:80px;top:1048px">
    <div class="orb"><svg><use href="#mic"/></svg></div>
    <div class="controls">
      <span class="control" aria-label="Delete last sentence"><svg><use href="#undo"/></svg></span>
      <span class="control" aria-label="Send and keep recording"><svg><use href="#stop"/></svg></span>
      <span class="control control--delete" aria-label="Delete"><svg><use href="#trash"/></svg></span>
    </div>
    <div class="send-pill">Send</div>
  </section>
  <section class="screen screen--transcript" style="left:446px;top:1176px">
    <div class="orb"><svg><use href="#mic"/></svg></div>
    <div class="transcript-card">
      <p class="transcript-text">Hi Sam, just leaving a quick note about tomorrow. The meeting moved to ten so we can grab coffee first. Let me know if that still works for you and the team.</p>
      <span class="card-action card-action--delete"><svg><use href="#trash"/></svg></span>
      <span class="card-action card-action--send"><svg><use href="#send"/></svg></span>
    </div>
  </section>
  <section class="screen screen--home" style="left:820px;top:1040px">
    <div class="orb"><svg><use href="#mic"/></svg></div>
    <p class="caption">Tap to record</p>
    <div class="contacts">
      <span class="avatar avatar--a">AL</span>
      <span class="avatar avatar--b">SM</span>
      <span class="avatar avatar--c">JO</span>
    </div>
  </section>
  <section class="screen screen--listening" style="left:820px;top:1672px">
    <div class="orb"><svg><use href="#play"/></svg></div>
    <p class="caption">New message from Alex</p>
    <div class="reactions" aria-label="Reply with an emoticon">
      <span class="reaction"><svg><use href="#heart"/></svg></span>
      <span class="reaction"><svg><use href="#tick"/></svg></span>
      <span class="reaction"><svg><use href="#star"/></svg></span>
      <span class="reaction"><svg><use href="#bolt"/></svg></span>
    </div>
  </section>
</main>
</body>
</html>
```